Bref créative
Business cards, stationary, envelopes for investment firm
Whitford Crest Holdings
Simple
Mark L. Tressel
Principal
4618 W. Pellham Avenue, Suite 207
Gilbert, AZ 85142
mark@whitfordch.com
www.whitfordch.com
Please provide a design that is clean and simple. Also, we require files with editable text as well.
Please use design logo in your design

```html
<!DOCTYPE html>
<html lang="en">
<head>
<meta charset="utf-8">
<title>Whitford Crest Holdings — Business Cards</title>
<link rel="stylesheet" href="https://fonts.googleapis.com/css2?family=Cinzel:wght@400;600&display=swap">
<style>
  :root {
    --navy: #2c3c8c;
    --ink: #3a3f4f;
    --paper: #ffffff;
    --backdrop: #c9cacc;
    --rule: #9aa0b4;
  }
  * { margin: 0; padding: 0; box-sizing: border-box; }
  html, body { width: 1200px; height: 895px; overflow: hidden; }
  body {
    background: var(--backdrop);
    font-family: "Cinzel", serif;
    color: var(--ink);
    position: relative;
  }
  .card {
    position: absolute;
    width: 560px;
    height: 320px;
    background: var(--paper);
    box-shadow: 0 6px 18px rgba(0,0,0,0.18);
  }
  /* Back card */
  .card-back { left: 570px; top: 80px; }
  .back-mark {
    position: absolute; left: 0; right: 0; top: 92px;
    display: flex; flex-direction: column; align-items: center;
  }
  .brand-dot {
    width: 64px; height: 64px; border-radius: 50%;
    background: var(--navy);
  }
  .back-name {
    margin-top: 14px; font-size: 15px; letter-spacing: 3px;
    color: var(--navy); font-weight: 400;
  }
  .back-web {
    margin-top: 14px; font-size: 12px; letter-spacing: 2px; color: var(--ink);
  }
  /* Front card */
  .card-front { left: 70px; top: 480px; }
  .edge-band {
    position: absolute; top: 0; bottom: 0; width: 16px; background: var(--navy);
  }
  .edge-band.left { left: 0; }
  .edge-band.right { right: 0; }
  .front-brand {
    position: absolute; left: 42px; top: 34px;
    display: flex; align-items: center; gap: 14px;
  }
  .front-brand .brand-dot { width: 50px; height: 50px; }
  .brand-name {
    color: var(--navy); font-weight: 400; line-height: 1.15;
  }
  .brand-name .line-main { display: block; font-size: 27px; letter-spacing: 1px; }
  .brand-name .line-sub { display: block; font-size: 13px; letter-spacing: 9px; }
  .person {
    position: absolute; right: 232px; top: 138px; text-align: right;
  }
  .person-name { font-size: 15px; font-weight: 600; letter-spacing: 1px; color: var(--ink); }
  .person-title { font-size: 11px; letter-spacing: 2px; margin-top: 4px; }
  .divider {
    position: absolute; left: 336px; top: 136px; width: 1px; height: 128px;
    background: var(--rule);
  }
  .contact-list {
    position: absolute; left: 350px; top: 136px; list-style: none;
  }
  .contact-list li {
    display: flex; align-items: center; gap: 8px;
    font-size: 11px; letter-spacing: 1px; height: 25px;
  }
  .contact-list svg { width: 15px; height: 15px; flex: none; }
  .address {
    position: absolute; left: 42px; top: 210px;
    font-size: 12px; letter-spacing: 1px; line-height: 1.7;
  }
</style>
</head>
<body>

<section class="card card-back" aria-label="Business card, back">
  <div class="back-mark">
    <div class="brand-dot"></div>
    <div class="back-name">WHITFORD CREST HOLDINGS</div>
    <div class="back-web">WWW.WHITFORDCH.COM</div>
  </div>
</section>

<section class="card card-front" aria-label="Business card, front">
  <div class="edge-band left"></div>
  <div class="edge-band right"></div>

  <div class="front-brand">
    <div class="brand-dot"></div>
    <div class="brand-name">
      <span class="line-main">WHITFORD CREST</span>
      <span class="line-sub">HOLDINGS</span>
    </div>
  </div>

  <div class="person">
    <div class="person-name">MARK L. TRESSEL</div>
    <div class="person-title">PRINCIPAL</div>
  </div>

  <div class="divider"></div>

  <ul class="contact-list">
    <li>
      <svg viewBox="0 0 16 16"><circle cx="8" cy="8" r="8" fill="#2c3c8c"/><path d="M5.5 4.2l1.3 1.5-.7 1a5 5 0 0 0 2.4 2.4l1-.7 1.5 1.3-.8 1.2C8 10.6 5.4 8 4.4 5l1.1-.8z" fill="#fff"/></svg>
      480-555-0147
    </li>
    <li>
      <svg viewBox="0 0 16 16"><circle cx="8" cy="8" r="8" fill="#2c3c8c"/><path d="M5.5 4.2l1.3 1.5-.7 1a5 5 0 0 0 2.4 2.4l1-.7 1.5 1.3-.8 1.2C8 10.6 5.4 8 4.4 5l1.1-.8z" fill="#fff"/></svg>
      480-555-0162
    </li>
    <li>
      <svg viewBox="0 0 16 16"><circle cx="8" cy="8" r="8" fill="#2c3c8c"/><path d="M5.5 4.2l1.3 1.5-.7 1a5 5 0 0 0 2.4 2.4l1-.7 1.5 1.3-.8 1.2C8 10.6 5.4 8 4.4 5l1.1-.8z" fill="#fff"/></svg>
      480-555-0189
    </li>
    <li>
      <svg viewBox="0 0 16 16"><circle cx="8" cy="8" r="8" fill="#2c3c8c"/><rect x="4" y="5.2" width="8" height="5.6" fill="none" stroke="#fff" stroke-width="1"/><path d="M4 5.4l4 3 4-3" fill="none" stroke="#fff" stroke-width="1"/></svg>
      MARK@WHITFORDCH.COM
    </li>
    <li>
      <svg viewBox="0 0 16 16"><circle cx="8" cy="8" r="8" fill="#2c3c8c"/><circle cx="8" cy="8" r="4" fill="none" stroke="#fff" stroke-width="1"/><path d="M4 8h8M8 4c-2 2.4-2 5.6 0 8M8 4c2 2.4 2 5.6 0 8" fill="none" stroke="#fff" stroke-width=".8"/></svg>
      WWW.WHITFORDCH.COM
    </li>
  </ul>

  <div class="address">
    4618 W. PELLHAM AVENUE, SUITE 207<br>
    GILBERT, AZ 85142
  </div>
</section>

</body>
</html>
```